Eco conscious print and frame company needs a website

‘LUMAeco is a new company that makes frames and fine art prints from sustainable bamboo. Our site should have an organic feel yet still have a professional clean look to it as well.
We need shopping cart and image uploading capabilities much like a pictorama or glowbird type of site only on a much smaller scale.
Currently we have 3 different styles available in sizes from 8"x8" all the way to 4ft by 8ft.
Target audience will be the snapvintra, pixelgram, zephone market.

Target Market(s)

20-40 years old male and female. Pixelgram generation.

Industry/Entity Type

Shopping

Requirements
Must have
• Front end and back end capabilities with emphasis on image uploading and shopping cart functionality.

```html
<!DOCTYPE html>
<html lang="en">
<head>
<meta charset="utf-8">
<title>LUMAeco Frame Company</title>
<link rel="stylesheet" href="https://fonts.googleapis.com/css2?family=Questrial&family=Open+Sans:wght@400;600;700&display=swap">
<style>
:root{
  --green:#6f9a2e;
  --green-dark:#557a1f;
  --green-light:#8cb43f;
  --lime-bg:#d4e8a8;
  --ink:#222;
  --muted:#555;
  --line:#d6d6d6;
  --panel:#f2f2f2;
  --red:#e8201c;
  --wood:#c79a6a;
  --wood-dark:#6e3a22;
}
*{box-sizing:border-box;margin:0;padding:0}
html,body{width:1068px;height:1200px;overflow:hidden;background:#fff}
body{position:relative;font-family:"Open Sans",Arial,sans-serif;color:var(--ink);font-size:10px}
.abs{position:absolute}
.heading{font-family:"Questrial",Arial,sans-serif}

.topbar{left:140px;top:0;width:787px;height:22px;background:#000;border-radius:0 0 12px 12px}
.social{top:4px;color:#fff;font-size:9px;display:flex;align-items:center;gap:5px}
.social i{display:inline-block;width:11px;height:11px;border-radius:2px}
.social-divider{left:786px;top:3px;width:1px;height:16px;background:#444}

.logo{left:140px;top:40px;display:flex;align-items:center;gap:8px}
.logo-dot{width:40px;height:40px;border-radius:50%;background:var(--green)}
.logo-name{font-family:"Questrial",sans-serif;font-size:28px;color:var(--green-dark)}

.search{left:582px;top:43px;width:191px;height:26px;border:1px solid #cfcfcf;border-radius:4px;background:#fff;font-size:9px;padding:8px 9px;color:#222}
.search-btn{right:4px;top:4px;width:17px;height:16px;background:#000;border-radius:2px}
.account{left:798px;top:45px;width:129px;height:21px;background:#1a1a1a;border-radius:4px;color:#fff;font-size:9px;display:flex;align-items:center;justify-content:center;gap:7px}
.upload{left:669px;top:88px;width:102px;height:18px;background:var(--green-light);color:#fff;font-size:9.5px;font-weight:600;display:flex;align-items:center;justify-content:center;gap:4px;border:1px solid var(--green)}
.upload b{display:inline-block;width:9px;height:9px;background:#fff;color:var(--green);font-size:9px;line-height:9px;text-align:center}
.cart{left:834px;top:91px;font-size:9px;color:#333;display:flex;align-items:center;gap:6px}

.nav{left:138px;top:130px;width:789px;height:27px;border-radius:5px;background:linear-gradient(#8cb43f,#5f8a24);display:flex;box-shadow:0 2px 3px rgba(0,0,0,.25)}
.nav a{color:#fff;text-decoration:none;font-size:10px;display:flex;align-items:center;justify-content:center;border-right:1px solid rgba(0,0,0,.18)}
.nav a:last-child{border-right:none}

.hero{left:138px;top:166px;width:789px;height:311px;border:1px solid var(--line);border-radius:4px}
.hero-panel{left:10px;top:8px;width:762px;height:211px;background:var(--panel);box-shadow:0 6px 6px -4px rgba(0,0,0,.45)}
.hero-title{left:173px;top:191px;font-size:24px;color:var(--green)}
.hero-sub{left:173px;top:219px;font-size:10.5px}
.features{left:210px;top:257px;list-style:none;font-size:10.5px}
.features li{height:24.6px;display:flex;align-items:center;gap:7px}
.tri{width:11px;height:11px;border-radius:50%;border:1px solid #bbb;background:#eee;position:relative;flex:none}
.tri:after{content:"";position:absolute;left:4px;top:2.5px;border-left:4px solid #777;border-top:2.5px solid transparent;border-bottom:2.5px solid transparent}
.hero-wood{left:500px;top:175px;width:192px;height:211px;background:linear-gradient(135deg,#e6c399,#b98a58 60%,#a8784a)}
.hero-photo{left:700px;top:175px;width:211px;height:211px;background:linear-gradient(160deg,#e6c3a0,#6a6a4a 40%,#4d5a2e 70%,#d9b58d)}
.dotline{left:151px;top:403px;width:760px;border-top:1px dotted #aaa}
.cats{left:151px;top:412px;width:760px;height:55px;display:flex}
.cat{width:127px;display:flex;align-items:center;gap:8px;padding-left:6px;font-size:9.5px;line-height:15px;border-right:1px dotted #ccc}
.cat:last-child{border-right:none}
.cat.active{background:#e4e4e4;width:120px;margin-right:7px}
.cat-img{width:36px;height:36px;flex:none}

.sizes{left:136px;top:497px;width:189px;height:114px;border:1px solid #ddd;background:#f4f4f4}
.sizes-head{left:4px;top:4px;width:181px;height:25px;background:var(--green);color:#fff;font-size:13px;padding:4px 7px}
.sizes-head:after{content:"";position:absolute;right:9px;bottom:-5px;border-top:5px solid var(--green);border-left:5px solid transparent;border-right:5px solid transparent}
.sizes ul{position:absolute;left:8px;top:32px;width:172px;list-style:none;font-size:10px}
.sizes li{height:26px;display:flex;align-items:center;gap:7px;border-bottom:1px solid #ddd}
.sizes li:last-child{border-bottom:none}

.banner{left:336px;top:513px;width:591px;height:76px;background:var(--lime-bg);text-align:center}
.banner-main{left:0;width:520px;top:12px;font-size:19.5px;color:var(--red)}
.banner-sub{left:0;width:520px;top:41px;font-size:16.5px;color:#111}
.badge{right:14px;top:7px;width:60px;height:60px;border-radius:50%;background:var(--green-light);border:3px solid #fff;color:#fff;font-size:11px;display:flex;align-items:center;justify-content:center;text-align:center;line-height:12px;transform:rotate(-20deg);box-shadow:0 3px 4px rgba(0,0,0,.2)}

.section-title{font-size:15px;color:var(--green)}
.section-title span{color:#111}
.box{border:1px solid #ddd;background:#fff}
.intro-text{left:10px;top:10px;width:258px;font-size:9.3px;line-height:18px;text-align:justify}
.intro-img{left:276px;top:0;width:95px;height:107px;background:linear-gradient(100deg,#b5785a,#6e3a22 50%,#4a2315)}
.testi-photo{left:12px;top:11px;width:91px;height:85px;border:1px solid #ccc;background:linear-gradient(#d9d2c6,#b48a68 55%,#2b2b2b)}
.testi-text{left:117px;top:16px;font-size:9.3px;line-height:18.5px}

.grid{left:137px;top:812px;width:786px;height:163px}
.frame-card{position:absolute;top:12px;width:104px;height:115px}
.frame-card.bamboo{background:linear-gradient(135deg,#edd2ac,#c49566 55%,#a67646)}
.frame-card.walnut{background:linear-gradient(100deg,#b2704e,#6e3a22 55%,#4a2315)}
.frame-label{position:absolute;top:141px;width:104px;text-align:center;font-size:9.5px}

.band{left:0;top:984px;width:1068px;height:216px;background:linear-gradient(#ececec,#fff 70%)}
.news-tab{left:138px;top:998px;width:98px;height:26px;background:var(--green);color:#fff;font-size:13.5px;padding:4px 10px}
.news-tab:after{content:"";position:absolute;right:6px;bottom:-5px;border-top:5px solid var(--green);border-left:5px solid transparent;border-right:5px solid transparent}
.news{left:138px;top:1024px;width:786px;height:83px;background:#fff;border:1px solid #ddd;display:flex}
.news-item{flex:1;display:flex;gap:12px;padding:25px 0 0 15px;border-right:1px solid #e2e2e2;margin:8px 0}
.news-item:last-child{border-right:none}
.news-thumb{width:38px;height:38px;flex:none;background:linear-gradient(#c9a08a,#6d4a38)}
.news-date{color:var(--green);font-size:10px;margin-top:-8px;margin-bottom:4px}
.news-copy{font-size:9px;line-height:15px;color:#444;width:175px}

.footer-links{left:0;width:1068px;top:1137px;text-align:center;font-size:9.3px;color:#333}
.footer-links span{color:#666;margin:0 6px}
.copyright{left:0;width:1068px;top:1156px;text-align:center;font-size:9px;color:#333}
.bottom-rule{left:0;top:1197px;width:1068px;height:3px;background:#111}
</style>
</head>
<body>

<div class="abs topbar"></div>
<div class="abs social" style="left:713px"><i style="background:#3b5a98"></i>Friendbook</div>
<div class="abs social-divider"></div>
<div class="abs social" style="left:801px"><i style="background:#35b3e0"></i>Follow us on Chirpline</div>

<div class="abs logo"><span class="logo-dot"></span><span class="logo-name">LUMAeco</span></div>

<div class="abs search">Search the Product
  <span class="abs search-btn">
    <svg width="17" height="16" viewBox="0 0 17 16"><circle cx="7.5" cy="7" r="3.6" fill="none" stroke="#fff" stroke-width="1.6"/><line x1="10" y1="9.6" x2="13" y2="12.6" stroke="#fff" stroke-width="1.8"/></svg>
  </span>
</div>
<div class="abs account"><span>Sign in</span>|<span>Sign Up</span>|<span>Help</span></div>
<div class="abs upload">UPLOAD PHOTOS <b>+</b></div>
<div class="abs cart">
  <svg width="18" height="12" viewBox="0 0 18 12"><path d="M1 1h3l2 7h9l2-5H5" fill="none" stroke="#999" stroke-width="1.3"/><circle cx="7" cy="10.5" r="1.2" fill="#999"/><circle cx="14" cy="10.5" r="1.2" fill="#999"/></svg>
  <span>Cart is Empty</span>
  <svg width="7" height="4" viewBox="0 0 7 4"><path d="M0 0h7L3.5 4z" fill="#333"/></svg>
</div>

<nav class="abs nav">
  <a style="width:82px">HOME</a>
  <a style="width:164px">PICTURE FRAME &amp; MOUNTS</a>
  <a style="width:155px">MULTI APERTURE FRAMES</a>
  <a style="width:115px">PRINT &amp; FRAME</a>
  <a style="width:104px">READY MADE</a>
  <a style="width:63px">FAQ</a>
  <a style="width:106px">CONTACT US</a>
</nav>

<section class="abs hero"><div class="abs hero-panel"></div></section>
<h1 class="abs heading hero-title" style="font-weight:400">Picture Frames / Mounts</h1>
<p class="abs hero-sub">Create your picture Frame &amp; Mount online. It's fun &amp; Easy...</p>
<ul class="abs features">
  <li><span class="tri"></span>Dispatched in 1-3 days</li>
  <li><span class="tri"></span>Hand Made in the UK</li>
  <li><span class="tri"></span>Over 500 Different Frames</li>
  <li><span class="tri"></span>Low Price Guarantee</li>
  <li><span class="tri"></span>Full Visualisation Online</li>
</ul>
<div class="abs hero-wood" role="img" aria-label="Close-up of a bamboo frame corner with a metal wing nut fastener"></div>
<div class="abs hero-photo" role="img" aria-label="Framed holiday photo of a child on a beach, mounted on bamboo"></div>
<div class="abs dotline"></div>
<div class="abs cats">
  <div class="cat active"><span class="cat-img" role="img" aria-label="Bamboo frame thumbnail" style="background:linear-gradient(135deg,#e1bf95,#a87a4a)"></span><span>Picture<br>Frames /<br>Mounts</span></div>
  <div class="cat"><span class="cat-img" role="img" aria-label="Canvas print thumbnail" style="background:linear-gradient(100deg,#a86a4a,#5a2d1a)"></span><span>Canvas<br>Printing<br>Service</span></div>
  <div class="cat"><span class="cat-img" role="img" aria-label="Digital print thumbnail" style="background:linear-gradient(135deg,#7a4a33,#d8c3b0)"></span><span>Digital<br>Print and<br>Frame</span></div>
  <div class="cat"><span class="cat-img" role="img" aria-label="Budget frame thumbnail" style="background:linear-gradient(135deg,#8a4a3a,#e6d6c6)"></span><span>Cheap<br>Picture<br>Frames</span></div>
  <div class="cat"><span class="cat-img" role="img" aria-label="Multi aperture frame thumbnail" style="background:linear-gradient(#e8c766,#c39a2e)"></span><span>Multi<br>Aperture<br>Frames</span></div>
  <div class="cat"><span class="cat-img" role="img" aria-label="Swept frame moulding thumbnail" style="background:linear-gradient(135deg,#8a8060,#cfc4a0)"></span><span>Swept<br>Picture<br>Frames</span></div>
</div>

<aside class="abs sizes">
  <div class="abs sizes-head heading">Frame Size</div>
  <ul>
    <li><span class="tri"></span>8"x8" Size</li>
    <li><span class="tri"></span>6"x8" Size</li>
    <li><span class="tri"></span>4"x8" Size</li>
  </ul>
</aside>

<div class="abs banner">
  <p class="abs heading banner-main">1-3 Day Dispatch On All Orders - Guaranteed.</p>
  <p class="abs heading banner-sub">Free Delivery on all Orders over £50 net</p>
  <div class="abs badge heading">Free<br>Delivery</div>
</div>

<h2 class="abs heading section-title" style="left:136px;top:632px;font-weight:400">Introducing <span>LUMAeco</span></h2>
<div class="abs box" style="left:136px;top:657px;width:372px;height:108px">
  <p class="abs intro-text">Lorem Ipsum is simply dummy text of the printing and typesetting industry. Lorem Ipsum has been the industry's standard dummy text ever since the 1500s, when an unknown printer took a galley of type and scrambled.</p>
  <div class="abs intro-img" role="img" aria-label="Walnut frame moulding detail"></div>
</div>

<h2 class="abs heading section-title" style="left:552px;top:632px;font-weight:400">Customer Testimonials</h2>
<div class="abs box" style="left:554px;top:657px;width:372px;height:108px">
  <div class="abs testi-photo" role="img" aria-label="Portrait of the customer"></div>
  <div class="abs testi-text">perb service? I ordered my frame online last Friday<br>afternoon.<br>Daniel R<br><b>Read More</b></div>
</div>

<h2 class="abs heading section-title" style="left:136px;top:785px;font-weight:400">Picture Frame Categories</h2>
<div class="abs box grid">
  <div class="frame-card bamboo" style="left:31px" role="img" aria-label="Light bamboo frame with wing nut"></div>
  <div class="frame-card walnut" style="left:183px" role="img" aria-label="Dark walnut frame moulding"></div>
  <div class="frame-card bamboo" style="left:334px" role="img" aria-label="Light bamboo frame with wing nut"></div>
  <div class="frame-card walnut" style="left:490px" role="img" aria-label="Dark walnut frame moulding"></div>
  <div class="frame-card bamboo" style="left:649px" role="img" aria-label="Light bamboo frame with wing nut"></div>
  <div class="frame-label" style="left:31px">Light Frames »</div>
  <div class="frame-label" style="left:183px">Light Frames »</div>
  <div class="frame-label" style="left:334px">Light Frames »</div>
  <div class="frame-label" style="left:490px">Light Frames »</div>
  <div class="frame-label" style="left:649px">Light Frames »</div>
</div>

<div class="abs band"></div>
<div class="abs news-tab heading">Latest News</div>
<div class="abs news">
  <div class="news-item"><div class="news-thumb" role="img" aria-label="News photo"></div><div><p class="news-date">20.10.2012</p><p class="news-copy">Lorem Ipsum is simply dummy text of the printing and typesetting industry</p></div></div>
  <div class="news-item"><div class="news-thumb" role="img" aria-label="News photo" style="background:linear-gradient(#8aa0c0,#3a3a4a)"></div><div><p class="news-date">20.10.2012</p><p class="news-copy">Lorem Ipsum is simply dummy text of the printing and typesetting industry</p></div></div>
  <div class="news-item"><div class="news-thumb" role="img" aria-label="News photo" style="background:linear-gradient(#7a5a48,#2a2220)"></div><div><p class="news-date">20.10.2012</p><p class="news-copy">Lorem Ipsum is simply dummy text of the printing and typesetting industry</p></div></div>
</div>

<p class="abs footer-links">Home<span>|</span>PICTURE FRAME &amp; MOUNTS<span>|</span>MULTI APERTURE FRAMES<span>|</span>PRINT &amp; FRAME<span>|</span>READY MADE<span>|</span>FAQ<span>|</span>Contact Us</p>
<p class="abs copyright">Copyrights @ 2012 All Rights Reserved</p>
<div class="abs bottom-rule"></div>

</body>
</html>
```